Cover für den Roman Marlene betritt die Bühne
Zielgruppe
Autorin einer belletristischen Erzählung über die Kunst der Moderne. Das Buch richtet sich an Leser die sich für Moderne Kunst interessieren.
Aufgabenstellung
Gesucht wird ein sehr zeitgemäßes und auffallendes Design, auch gerne mit einer starken Hintergrundfarbe. Der Leser soll auf den ersten Blick erkennen können, dass es hier um Kunst geht (Lorenz Aubach, Tarnowski, Ferrandi Hadley, etc). Bitte unbedingt alle Lizenzrechte abklären und keine Originalwerke verwenden.
Eine Idee wäre einen Bezug zu "Marlene und der Barastides" herzustellen. (Vielzitiertes Thema in der Kunstgeschichte, Marlene schlägt dem Feldherrn Barastides den Kopf ab und befreit ihr Volk.)
Das Design sollte aber trotzdem nett und nicht gruselig sein.
Ganz wichtig keine nackte Marlene. Sie ist stark und emanzipiert sich!
Text auf der Vorderseite:
Olga Mertelhuber
Marlene betritt die Bühne
Erzählung über die Kunst der Moderne
Text auf der Rückseite:
kurze Inhaltsangabe
Das Cover soll für ein Taschenbuch als auch ein e-book funktionieren

```html
<!DOCTYPE html>
<html lang="de">
<head>
<meta charset="utf-8">
<title>Marlene betritt die Bühne – Cover</title>
<link rel="stylesheet" href="https://fonts.googleapis.com/css2?family=Montserrat:wght@700;800;900&display=swap">
<style>
  :root {
    --ink: #111115;
    --cream: #f5e8d8;
    --frame-red: #cc5545;
    --title-cream: #f3e6d2;
    --accent-red: #e0282c;
    --sky: #92b0dc;
    --paper: #ffffff;
  }
  * { margin: 0; padding: 0; box-sizing: border-box; }
  html, body {
    width: 803px; height: 1200px; overflow: hidden;
    background: var(--paper);
  }
  .cover {
    position: relative;
    width: 803px; height: 1200px;
    background: var(--ink);
    font-family: "Montserrat", sans-serif;
    overflow: hidden;
  }
  .author-band {
    position: absolute; left: 0; top: 0; width: 100%; height: 62px;
    display: flex; align-items: center; justify-content: center;
  }
  .author-name {
    color: var(--title-cream);
    font-weight: 800; font-size: 24px; letter-spacing: 0.3px;
    text-transform: uppercase;
  }
  .canvas-field {
    position: absolute; left: 0; top: 62px; width: 778px; height: 866px;
    background: var(--cream);
  }
  .picture-frame {
    position: absolute; left: 86px; top: 78px; width: 642px; height: 808px;
    border: 18px solid var(--frame-red);
    background: var(--cream);
  }
  .artwork {
    position: absolute; inset: 12px;
    background: linear-gradient(160deg, var(--sky) 0%, #e8e0d4 40%, #d8352c 65%, var(--ink) 85%, #6aa8d0 100%);
  }
  .title-block {
    position: absolute; left: 52px; top: 1000px;
    transform: rotate(-12deg); transform-origin: left top;
    color: var(--title-cream);
    font-weight: 800; font-size: 56px; line-height: 0.95;
    text-transform: uppercase;
  }
  .title-block span { display: block; }
  .title-block .line-2 { margin-left: 44px; }
  .title-block .line-3 { margin-left: 118px; }
  .subtitle {
    position: absolute; left: 510px; top: 1068px;
    color: var(--accent-red);
    font-weight: 800; font-size: 22px; line-height: 1.12;
    text-transform: uppercase;
  }
  .subtitle span { display: block; }
</style>
</head>
<body>
  <main class="cover">
    <header class="author-band">
      <p class="author-name">Olga Mertelhuber</p>
    </header>

    <section class="canvas-field">
      <div class="picture-frame">
        <div class="artwork" role="img" aria-label="Illustration im Stil der Moderne: Marlene mit goldenem Schwert steigt aus einem Bilderrahmen, vor blauem Himmel und rot-schwarz gestreiften Flächen"></div>
      </div>
    </section>

    <h1 class="title-block">
      <span class="line-1">Marlene</span>
      <span class="line-2">betritt</span>
      <span class="line-3">die Bühne</span>
    </h1>

    <p class="subtitle">
      <span>Erzählung über</span>
      <span>die Kunst</span>
      <span>der Moderne</span>
    </p>
  </main>
</body>
</html>
```